Stationery Design Project

We are interested in A4 paper letterheads, envelopes, maybe A4 folders where we can put the patients' results in and businesscards. No information will be given out for the time being.
We would like to see mainly shades of white.. please refer to
http://en.huevaultix.org/wiki/Category:Shades_of_white
anti-flash white, splashed white,ghost white, ivory, snow and white smoke or even light grey
we are interested mainly on the silver design but we welcome the other colors as well. Since its about a gynecologist please avoid dark colors, instead use shades of beige, light grey and white

```html
<!DOCTYPE html>
<html lang="en">
<head>
<meta charset="utf-8">
<title>Stationery Design Project</title>
<link rel="stylesheet" href="https://fonts.googleapis.com/css2?family=Cinzel:wght@400&family=Arimo:wght@400&display=swap">
<style>
  :root {
    --gold: #d9a200;
    --gold-deep: #c99400;
    --gold-light: #e9b200;
    --beige: #e7cf8e;
    --beige-light: #f2e0a6;
    --paper: #ffffff;
    --ink-grey: #6d6d6d;
    --board-light: #8a8b89;
    --board-dark: #3f403f;
    --footer: #0d0d0d;
  }
  * { margin: 0; padding: 0; box-sizing: border-box; }
  html, body { width: 1200px; height: 848px; overflow: hidden; }
  body {
    position: relative;
    background: radial-gradient(ellipse 900px 620px at 330px 260px, var(--board-light), var(--board-dark));
    font-family: "Cinzel", serif;
  }
  .corner-band {
    position: absolute; left: -60px; top: -40px; width: 330px; height: 48px;
    background: #0a0a0a; transform: rotate(-27deg); transform-origin: left top;
  }
  .sheet { position: absolute; background: var(--paper); box-shadow: 0 2px 6px rgba(0,0,0,.35); overflow: hidden; }

  .mark { display: block; background: linear-gradient(160deg, var(--gold-light), var(--gold-deep)); }
  .brand-name { color: var(--gold); font-size: 15px; letter-spacing: .5px; line-height: 1; white-space: nowrap; }
  .brand-slogan { color: var(--gold); font-size: 6px; text-align: right; letter-spacing: .3px; margin-top: 3px; }
  .contact { color: var(--ink-grey); font-size: 6.5px; text-align: right; line-height: 1.2; letter-spacing: .3px; margin-top: 5px; }

  .brand-row { display: flex; align-items: flex-start; gap: 4px; }
  .brand-text { padding-top: 11px; }

  /* business card front */
  .card-front { left: 57px; top: 68px; width: 242px; height: 143px;
    background: linear-gradient(180deg, #e9d6a0, #dcc17a); }
  .card-front .mark { position: absolute; left: 88px; top: 29px; width: 67px; height: 67px; }
  .card-front .mark-reflection { position: absolute; left: 88px; top: 96px; width: 67px; height: 20px;
    background: linear-gradient(180deg, rgba(217,162,0,.35), rgba(217,162,0,0)); }

  /* business card back */
  .card-back { left: 332px; top: 68px; width: 241px; height: 143px; }
  .card-back .brand-row { position: absolute; left: 61px; top: 15px; }
  .card-back .mark { width: 30px; height: 30px; }
  .card-back .brand-text { padding-top: 11px; }
  .card-back .brand-name { font-size: 11px; }
  .card-back .brand-slogan { font-size: 5px; }
  .card-back .person { position: absolute; left: 0; right: 0; top: 63px; text-align: center; }
  .person-name { color: var(--ink-grey); font-size: 11px; letter-spacing: .5px; }
  .person-title { color: #9a9a9a; font-size: 4.5px; letter-spacing: 3px; margin-top: 4px; }
  .card-back .details { position: absolute; left: 0; right: 0; top: 102px; text-align: center;
    color: var(--ink-grey); font-size: 4.5px; line-height: 1.45; letter-spacing: .2px; }

  /* envelope front */
  .envelope-front { left: 56px; top: 235px; width: 517px; height: 265px; }
  .envelope-front .brand-row { position: absolute; left: 43px; top: 36px; }
  .envelope-front .mark { width: 37px; height: 37px; }
  .envelope-front .brand-text { padding-top: 14px; }

  /* envelope back */
  .envelope-back { left: 56px; top: 512px; width: 517px; height: 263px; }
  .envelope-back svg { position: absolute; left: 0; top: 0; }

  /* letterhead */
  .letterhead { left: 601px; top: 68px; width: 548px; height: 707px; }
  .letterhead .brand-row { position: absolute; left: 36px; top: 35px; }
  .letterhead .mark { width: 42px; height: 42px; }
  .letterhead .brand-text { padding-top: 16px; }
  .letterhead .brand-name { font-size: 16px; }
  .letterhead-band { position: absolute; left: 0; bottom: 0; width: 100%; height: 61px;
    background: linear-gradient(100deg, var(--beige) 0%, var(--beige-light) 45%, #f7e7b8 70%, var(--beige) 100%);
    display: flex; align-items: center; justify-content: flex-end; padding-right: 22px; }
  .band-name { color: var(--gold); opacity: .45; font-size: 12px; letter-spacing: .5px; }

  .footer { position: absolute; left: 0; bottom: 0; width: 1200px; height: 56px; background: var(--footer);
    display: flex; align-items: center; padding-left: 62px; }
  .footer-title { color: #ffffff; font-family: "Arimo", sans-serif; font-size: 16px; }
</style>
</head>
<body>
  <div class="corner-band"></div>

  <section class="sheet card-front">
    <span class="mark"></span>
    <span class="mark-reflection"></span>
  </section>

  <section class="sheet card-back">
    <div class="brand-row">
      <span class="mark"></span>
      <div class="brand-text">
        <div class="brand-name">Company name</div>
        <div class="brand-slogan">company slogan</div>
      </div>
    </div>
    <div class="person">
      <div class="person-name">John Doe</div>
      <div class="person-title">YOUR JOB TITLE HERE</div>
    </div>
    <div class="details">
      Company address<br>
      Phone : 01234 567 89 | Fax : 01234 567 89<br>
      johndoe@companyname.com | www.yourcompanyname.com
    </div>
  </section>

  <section class="sheet envelope-front">
    <div class="brand-row">
      <span class="mark"></span>
      <div class="brand-text">
        <div class="brand-name">Company name</div>
        <div class="brand-slogan">company slogan</div>
        <div class="contact">Company address<br>Phone : 01234 567 89<br>Fax : 01234 567 89<br>www.yourcompanynmae.com</div>
      </div>
    </div>
  </section>

  <section class="sheet envelope-back">
    <svg width="517" height="263" viewBox="0 0 517 263">
      <defs>
        <linearGradient id="flapGold" x1="0" y1="0" x2="1" y2="0.3">
          <stop offset="0" stop-color="#e8b400"/>
          <stop offset="0.35" stop-color="#f0c640"/>
          <stop offset="0.6" stop-color="#dca600"/>
          <stop offset="1" stop-color="#e9b300"/>
        </linearGradient>
        <linearGradient id="squareGold" x1="0" y1="0" x2="1" y2="1">
          <stop offset="0" stop-color="#e9b200"/>
          <stop offset="1" stop-color="#c99400"/>
        </linearGradient>
      </defs>
      <polygon points="0,0 517,0 517,52 258,83 0,52" fill="url(#flapGold)"/>
      <rect x="236" y="11" width="43" height="43" fill="url(#squareGold)"/>
      <rect x="236" y="54" width="43" height="14" fill="#d9a200" opacity="0.3"/>
    </svg>
  </section>

  <section class="sheet letterhead">
    <div class="brand-row">
      <span class="mark"></span>
      <div class="brand-text">
        <div class="brand-name">Company name</div>
        <div class="brand-slogan">company slogan</div>
        <div class="contact">Company address<br>Phone : 01234 567 89<br>Fax : 01234 567 89<br>www.yourcompanynmae.com</div>
      </div>
    </div>
    <div class="letterhead-band">
      <span class="band-name">Company name</span>
    </div>
  </section>

  <footer class="footer">
    <span class="footer-title">Stationery Design Project</span>
  </footer>
</body>
</html>
```